Corporate Identity Pack - LetterHead, Business Card, Envelope

We are looking for a clean, professional, and visually connected corporate identity set for our company "MERIDA CARE" (Cleaning, Gardening, and Pest Control services).

The pack must include:

Business Card (front and back)
Envelope with recipient window on the right side (22x11)
A4 Letterhead

We provide:
Our final logo (PNG)
Three design references (Inspiration1, Inspiration2, Inspiration3) to spark ideas — but you are absolutely free to propose your own creative solutions based on these concepts.

What we want:
A clean, modern, and trustworthy style
A subtle but creative watermark or graphic detail on the letterhead (not too invasive)

The same visual "family feeling" across business card, envelope, and letterhead: designs must be different but clearly connected

Strong readability for all text and contact details

Use our brand colors (Navy Blue, Green, Orange/Red) in a smart, non-overloaded way

No strict limitations: we are open to creative proposals as long as they are coherent, elegant, and suitable for professional use

Technical specifications:
100% full A4 page layout (no accidental borders)

Deliver ready-to-print PDFs and vector files (AI, EPS)

Respect 5 mm safety margins

Standard sizes for A4, business card, envelope C6 with window at the right

Tone:
Modern – Clean – Elegant – Creative – Trustworthy

Target Market(s)

Professional businesses, property managers, condominium administrators, companies, clinics, and offices requiring cleaning, gardening, and pest control services. The design must convey trust, reliability, professionalism, and attention to detail.

Industry/Entity Type

Cleaning Services, Gardening Services, Pest Control Services

Colors
0054AA
0677BA
7BADD7
CADEEF
E8F1F8
59FF00
82FF00
B8FF75
E3FFCB
F4FFEA
EB3D1F
EC4F4E
F09395
F8D3D4
FCEDEE

Requirements
Must have
• Cohesive design across business card, letterhead, and envelope Clean, modern, professional look Use of brand colors: Navy Blue (main), Green, Orange/Red accents Letterhead must include a subtle watermark without interfering with text Envelope must be with a transparent window for recipient address visibility High readability of all text and contact details Proper alignment, no unnecessary margins (full A4 layout)
Nice to have
• Creative but discreet use of the checkmark from the logo as part of the background or watermark Slight variation or accent of color tones while respecting brand identity A clean visual accent that gives a sense of movement or dynamic professionalism (without being distracting) Icons for email, phone, and website on the business card (if stylistically appropriate)
Should not have
• Overuse of colors or rainbow effects Heavy backgrounds or complex textures that interfere with readability Fonts that are too playful, comic-style, or non-professional Overcrowded layouts — the design must feel clean and spacious Watermarks that are too strong or central (they must be subtle and marginal)

```html
<!DOCTYPE html>
<html lang="en">
<head>
<meta charset="utf-8">
<title>Merida Care – Letterhead</title>
<link rel="stylesheet" href="https://fonts.googleapis.com/css2?family=Open+Sans:wght@400;600;700;800&family=Roboto:wght@400;500&display=swap">
<style>
  :root {
    --backdrop: #e7e8ea;
    --paper: #ffffff;
    --navy: #24215f;
    --green: #7bc143;
    --orange: #f26522;
    --ink: #555a60;
    --ink-soft: #6b7076;
    --wash-navy: rgba(36, 33, 95, 0.07);
    --wash-green: rgba(123, 193, 67, 0.08);
  }
  * { margin: 0; padding: 0; box-sizing: border-box; }
  html, body { width: 1200px; height: 1000px; overflow: hidden; }
  body {
    background: var(--backdrop);
    font-family: "Open Sans", Arial, sans-serif;
    position: relative;
  }
  .letterhead {
    position: absolute;
    top: 218px;
    width: 439px;
    height: 564px;
    background: var(--paper);
    box-shadow: 3px 4px 8px rgba(0, 0, 0, 0.18);
    overflow: hidden;
  }
  .letterhead--green { left: 155px; }
  .letterhead--navy { left: 606px; }

  .brand {
    position: absolute;
    left: 45px;
    top: 45px;
    display: flex;
    align-items: center;
    gap: 7px;
  }
  .brand__square {
    width: 20px;
    height: 20px;
    background: var(--navy);
  }
  .brand__name {
    font-weight: 700;
    font-size: 18px;
    letter-spacing: -0.3px;
    color: var(--navy);
    line-height: 1;
  }

  .contacts {
    position: absolute;
    left: 308px;
    top: 33px;
    list-style: none;
    font-size: 7.4px;
    color: var(--ink);
  }
  .contacts li {
    display: flex;
    align-items: center;
    gap: 4px;
    height: 11.2px;
  }
  .contacts svg { width: 8px; height: 8px; flex: none; }

  .letter {
    position: absolute;
    left: 45px;
    top: 131px;
    width: 349px;
    font-size: 6.55px;
    line-height: 9.2px;
    color: var(--ink);
    text-align: justify;
  }
  .letter__greeting { margin-bottom: 9px; }
  .letter__paragraph { margin-bottom: 9.5px; }
  .letter__closing { margin-top: 0; }

  .watermark {
    position: absolute;
    left: 125px;
    top: 187px;
    width: 191px;
    height: 191px;
    background: linear-gradient(180deg, var(--wash-navy) 0%, var(--wash-navy) 55%, var(--wash-green) 100%);
  }

  .signatory {
    position: absolute;
    left: 45px;
    top: 397px;
    font-size: 6.8px;
    line-height: 9.6px;
    color: var(--ink);
  }
  .signature {
    position: absolute;
    left: 45px;
    top: 422px;
    width: 40px;
    height: 38px;
    background: linear-gradient(135deg, #f1f1f1, #dcdcdc);
  }

  .footer {
    position: absolute;
    left: 0;
    bottom: 0;
    width: 100%;
    height: 30px;
    font-family: "Roboto", Arial, sans-serif;
    color: #ffffff;
    font-size: 6.1px;
    line-height: 8px;
    text-align: center;
    padding: 6px 0 0 40px;
  }
  .letterhead--green .footer { background: var(--green); }
  .letterhead--navy .footer { background: var(--navy); }
  .footer__company { color: var(--orange); font-weight: 500; }
  .footer__corner {
    position: absolute;
    left: 0;
    bottom: 0;
    width: 30px;
    height: 30px;
    background: var(--paper);
  }
  .footer__corner-square {
    position: absolute;
    left: 2px;
    bottom: 2px;
    width: 10px;
    height: 10px;
    background: var(--orange);
  }
</style>
</head>
<body>

<section class="letterhead letterhead--green">
  <div class="brand">
    <span class="brand__square"></span>
    <span class="brand__name">MERIDA CARE</span>
  </div>
  <ul class="contacts">
    <li><svg viewBox="0 0 8 8"><rect width="8" height="8" rx="1" fill="#f26522"/><rect x="2.6" y="1.4" width="2.8" height="5.2" rx="0.5" fill="none" stroke="#fff" stroke-width="0.8"/></svg>+39 320 5550148</li>
    <li><svg viewBox="0 0 8 8"><rect width="8" height="8" rx="1" fill="#f26522"/><rect x="1.5" y="2.2" width="5" height="3.6" fill="none" stroke="#fff" stroke-width="0.7"/><path d="M1.5 2.2 L4 4.3 L6.5 2.2" fill="none" stroke="#fff" stroke-width="0.7"/></svg>office@merida-care.srl</li>
    <li><svg viewBox="0 0 8 8"><rect width="8" height="8" rx="1" fill="#f26522"/><rect x="1.5" y="2.2" width="5" height="3.6" fill="none" stroke="#fff" stroke-width="0.7"/><path d="M1.5 2.2 L4 4.3 L6.5 2.2" fill="none" stroke="#fff" stroke-width="0.7"/></svg>info.meridacare@pec.it</li>
    <li><svg viewBox="0 0 8 8"><rect width="8" height="8" rx="1" fill="#f26522"/><circle cx="4" cy="4" r="2.4" fill="none" stroke="#fff" stroke-width="0.7"/><path d="M1.6 4 H6.4 M4 1.6 V6.4" stroke="#fff" stroke-width="0.5"/></svg>www.merida-care.srl</li>
  </ul>

  <div class="watermark" aria-hidden="true"></div>

  <div class="letter">
    <p class="letter__greeting">Dear customer,</p>
    <p class="letter__paragraph">Lorem ipsum dolor sit amet, consectetur adipisicing elit, sed do eiusmod tempor incididunt ut labore et dolore magna aliqua. Ut enim ad minim veniam, quis nostrud exercitation ullamco laboris nisi ut aliquip ex ea commodo consequat. Duis aute irure dolor in reprehenderit in voluptate velit esse cillum dolore eu fugiat nulla pariatur. Excepteur sint occaecat cupidatat non proident, sunt in culpa qui officia deserunt mollit anim id est laborum.</p>
    <p class="letter__paragraph">Lorem ipsum dolor sit amet, consectetur adipisicing elit, sed do eiusmod tempor incididunt ut labore et dolore magna aliqua. Ut enim ad minim veniam, quis nostrud exercitation ullamco laboris nisi ut aliquip ex ea commodo consequat. Duis aute irure dolor in reprehenderit in voluptate velit esse cillum dolore eu fugiat nulla pariatur. Excepteur sint occaecat cupidatat non proident, sunt in culpa qui officia deserunt mollit anim id est laborum.</p>
    <p class="letter__paragraph">Lorem ipsum dolor sit amet, consectetur adipisicing elit, sed do eiusmod tempor incididunt ut labore et dolore magna aliqua. Ut enim ad minim veniam, quis nostrud exercitation ullamco laboris nisi ut aliquip ex ea commodo consequat. Duis aute irure dolor in reprehenderit in voluptate velit esse cillum dolore eu fugiat nulla pariatur. Excepteur sint occaecat cupidatat non proident, sunt in culpa qui officia deserunt mollit anim id est laborum.</p>
    <p class="letter__paragraph">Lorem ipsum dolor sit amet, consectetur adipisicing elit, sed do eiusmod tempor incididunt ut labore et dolore magna aliqua. Ut enim ad minim veniam, quis nostrud exercitation ullamco laboris nisi ut aliquip ex ea commodo consequat. Duis aute irure dolor in reprehenderit.</p>
    <p class="letter__closing">Yours Sincerely,</p>
  </div>

  <div class="signatory">
    <p>Luca Ferri</p>
    <p>General Director</p>
  </div>
  <div class="signature" role="img" aria-label="Handwritten signature of the General Director"></div>

  <footer class="footer">
    <p><span class="footer__company">Merida Care srl</span> Società unipersonale - Einzelunternehmen</p>
    <p>Via Monte Verde 24 - 39100 Bolzano (Bz) - REA Nr. Bz 105732 - P.I. - MwSt. 04418870215</p>
    <span class="footer__corner"><span class="footer__corner-square"></span></span>
  </footer>
</section>

<section class="letterhead letterhead--navy">
  <div class="brand">
    <span class="brand__square"></span>
    <span class="brand__name">MERIDA CARE</span>
  </div>
  <ul class="contacts">
    <li><svg viewBox="0 0 8 8"><rect width="8" height="8" rx="1" fill="#f26522"/><rect x="2.6" y="1.4" width="2.8" height="5.2" rx="0.5" fill="none" stroke="#fff" stroke-width="0.8"/></svg>+39 320 5550148</li>
    <li><svg viewBox="0 0 8 8"><rect width="8" height="8" rx="1" fill="#f26522"/><rect x="1.5" y="2.2" width="5" height="3.6" fill="none" stroke="#fff" stroke-width="0.7"/><path d="M1.5 2.2 L4 4.3 L6.5 2.2" fill="none" stroke="#fff" stroke-width="0.7"/></svg>office@merida-care.srl</li>
    <li><svg viewBox="0 0 8 8"><rect width="8" height="8" rx="1" fill="#f26522"/><rect x="1.5" y="2.2" width="5" height="3.6" fill="none" stroke="#fff" stroke-width="0.7"/><path d="M1.5 2.2 L4 4.3 L6.5 2.2" fill="none" stroke="#fff" stroke-width="0.7"/></svg>info.meridacare@pec.it</li>
    <li><svg viewBox="0 0 8 8"><rect width="8" height="8" rx="1" fill="#f26522"/><circle cx="4" cy="4" r="2.4" fill="none" stroke="#fff" stroke-width="0.7"/><path d="M1.6 4 H6.4 M4 1.6 V6.4" stroke="#fff" stroke-width="0.5"/></svg>www.merida-care.srl</li>
  </ul>

  <div class="watermark" aria-hidden="true"></div>

  <div class="letter">
    <p class="letter__greeting">Dear customer,</p>
    <p class="letter__paragraph">Lorem ipsum dolor sit amet, consectetur adipisicing elit, sed do eiusmod tempor incididunt ut labore et dolore magna aliqua. Ut enim ad minim veniam, quis nostrud exercitation ullamco laboris nisi ut aliquip ex ea commodo consequat. Duis aute irure dolor in reprehenderit in voluptate velit esse cillum dolore eu fugiat nulla pariatur. Excepteur sint occaecat cupidatat non proident, sunt in culpa qui officia deserunt mollit anim id est laborum.</p>
    <p class="letter__paragraph">Lorem ipsum dolor sit amet, consectetur adipisicing elit, sed do eiusmod tempor incididunt ut labore et dolore magna aliqua. Ut enim ad minim veniam, quis nostrud exercitation ullamco laboris nisi ut aliquip ex ea commodo consequat. Duis aute irure dolor in reprehenderit in voluptate velit esse cillum dolore eu fugiat nulla pariatur. Excepteur sint occaecat cupidatat non proident, sunt in culpa qui officia deserunt mollit anim id est laborum.</p>
    <p class="letter__paragraph">Lorem ipsum dolor sit amet, consectetur adipisicing elit, sed do eiusmod tempor incididunt ut labore et dolore magna aliqua. Ut enim ad minim veniam, quis nostrud exercitation ullamco laboris nisi ut aliquip ex ea commodo consequat. Duis aute irure dolor in reprehenderit in voluptate velit esse cillum dolore eu fugiat nulla pariatur. Excepteur sint occaecat cupidatat non proident, sunt in culpa qui officia deserunt mollit anim id est laborum.</p>
    <p class="letter__paragraph">Lorem ipsum dolor sit amet, consectetur adipisicing elit, sed do eiusmod tempor incididunt ut labore et dolore magna aliqua. Ut enim ad minim veniam, quis nostrud exercitation ullamco laboris nisi ut aliquip ex ea commodo consequat. Duis aute irure dolor in reprehenderit.</p>
    <p class="letter__closing">Yours Sincerely,</p>
  </div>

  <div class="signatory">
    <p>Luca Ferri</p>
    <p>General Director</p>
  </div>
  <div class="signature" role="img" aria-label="Handwritten signature of the General Director"></div>

  <footer class="footer">
    <p><span class="footer__company">Merida Care srl</span> Società unipersonale - Einzelunternehmen</p>
    <p>Via Monte Verde 24 - 39100 Bolzano (Bz) - REA Nr. Bz 105732 - P.I. - MwSt. 04418870215</p>
    <span class="footer__corner"><span class="footer__corner-square"></span></span>
  </footer>
</section>

</body>
</html>
```